We have a new logo so we need to change our business card

We're super Happy with our current cards but I think with a new logo should come a new design. I wouldn't mind seeing the icons that we used on the back last time reused on this card. Please feel free to visit our website to get a sense for our brand www.pawlowtide.ca

I need the final final to have contact info for:

Derek Osgood
Co-Owner
info@pawlowtide.ca
604-315-2780

and

Melissa Osgood
Co-Owner
info@pawlowtide.ca
604-347-5138

Target Market(s)

Female dog owners, 21 to 70

Industry/Entity Type

pet industry

Contact Information for Business Card

included in brief

Requirements
Should not have
• We do not want it to look cartonish

```html
<!DOCTYPE html>
<html lang="en">
<head>
<meta charset="utf-8">
<title>Pawlowtide Business Card</title>
<link rel="stylesheet" href="https://fonts.googleapis.com/css2?family=Open+Sans:wght@400;700&family=Arimo:wght@400&display=swap">
<style>
  :root {
    --backdrop: #cfcfcf;
    --card: #2a2a2a;
    --card-edge: #7dc75a;
    --accent: #7dc75a;
    --text-light: #e6e6e6;
    --text-muted: #c9c9c9;
    --divider: #4a4a4a;
    --emboss: #161616;
  }
  * { box-sizing: border-box; margin: 0; padding: 0; }
  html, body { width: 1200px; height: 800px; overflow: hidden; }
  body {
    background: var(--backdrop);
    display: flex;
    align-items: center;
    justify-content: center;
    gap: 48px;
  }
  .card {
    position: relative;
    width: 540px;
    height: 309px;
    background: var(--card);
    border-bottom: 3px solid var(--card-edge);
    box-shadow: 0 10px 24px rgba(0,0,0,0.25);
  }
  .card-front { display: flex; align-items: center; }
  .brand {
    display: flex;
    align-items: center;
    gap: 10px;
    width: 262px;
    padding-left: 28px;
  }
  .brand-mark {
    width: 48px; height: 48px;
    border-radius: 50%;
    background: var(--accent);
    flex: none;
  }
  .brand-name {
    font-family: "Open Sans", sans-serif;
    font-weight: 700;
    font-size: 27px;
    letter-spacing: -0.5px;
    color: var(--text-light);
    white-space: nowrap;
  }
  .divider {
    width: 1px;
    height: 150px;
    background: var(--divider);
    flex: none;
  }
  .contact {
    padding-left: 22px;
    font-family: "Arimo", sans-serif;
    color: var(--text-light);
  }
  .contact-name {
    font-family: "Open Sans", sans-serif;
    font-weight: 700;
    font-size: 22px;
    color: var(--accent);
    line-height: 1.05;
  }
  .contact-role {
    font-size: 15px;
    color: var(--text-muted);
    margin-bottom: 12px;
  }
  .contact-list { list-style: none; }
  .contact-list li {
    display: flex;
    align-items: center;
    gap: 8px;
    font-size: 14px;
    line-height: 20px;
    white-space: nowrap;
  }
  .contact-list.social { margin-top: 10px; }
  .contact-icon { width: 13px; height: 13px; flex: none; }
  .social-dot {
    width: 11px; height: 11px;
    border-radius: 50%;
    background: var(--accent);
    flex: none;
    margin: 0 1px;
  }
  .card-back {
    display: flex;
    align-items: center;
    justify-content: center;
  }
  .card-back .brand { width: auto; padding: 0; gap: 16px; }
  .card-back .brand-mark {
    width: 76px; height: 76px;
    background: var(--emboss);
  }
  .card-back .brand-name {
    font-size: 44px;
    color: var(--emboss);
  }
</style>
</head>
<body>
  <section class="card card-front">
    <div class="brand">
      <span class="brand-mark"></span>
      <span class="brand-name">Pawlowtide</span>
    </div>
    <div class="divider"></div>
    <div class="contact">
      <p class="contact-name">Derek Osgood</p>
      <p class="contact-role">Co-Owner</p>
      <ul class="contact-list">
        <li>
          <svg class="contact-icon" viewBox="0 0 24 24"><path fill="var(--accent)" d="M6.6 10.8a15.1 15.1 0 0 0 6.6 6.6l2.2-2.2a1 1 0 0 1 1-.25 11.4 11.4 0 0 0 3.6.57 1 1 0 0 1 1 1V20a1 1 0 0 1-1 1A17 17 0 0 1 3 4a1 1 0 0 1 1-1h3.5a1 1 0 0 1 1 1 11.4 11.4 0 0 0 .57 3.6 1 1 0 0 1-.25 1z"/></svg>
          604-315-2780
        </li>
        <li>
          <svg class="contact-icon" viewBox="0 0 24 24"><path fill="var(--accent)" d="M2 5h20v14H2z"/><path fill="none" stroke="var(--card)" stroke-width="2" d="M2 5l10 8 10-8"/></svg>
          info@pawlowtide.ca
        </li>
        <li>
          <svg class="contact-icon" viewBox="0 0 24 24"><g fill="none" stroke="var(--accent)" stroke-width="2"><circle cx="12" cy="12" r="10"/><path d="M2 12h20M12 2c3 3 3 17 0 20M12 2c-3 3-3 17 0 20"/></g></svg>
          www.pawlowtide.ca
        </li>
      </ul>
      <ul class="contact-list social">
        <li><span class="social-dot"></span>www.friendloop.com/pawlowtide</li>
        <li><span class="social-dot"></span>pawlowtide</li>
      </ul>
    </div>
  </section>

  <section class="card card-back">
    <div class="brand">
      <span class="brand-mark"></span>
      <span class="brand-name">Pawlowtide</span>
    </div>
  </section>
</body>
</html>
```